Landscape Contractor in need of New Web Design

HELP.. Please Help!!!!. Our current website is old, outdated, ugly... and well nothing like us.... so we are looking for someone to help build a new website that fits our company direction. We are a landscape company with multiple locations in order to meet the needs of our clients and their projects throughout the midwest. When most people think of landscaping, they think of mowing grandmas yard, but that is NOT even remotely close to what we do. We are 100% a commercial landscape company meaning we complete landscape and irrigation services for large scale commercial projects. We are looking for a website to showcase our commercial talents and awesome team of people.
Updates

Address of current website is www.plovermeadowco.com

```html
<!DOCTYPE html>
<html lang="en">
<head>
<meta charset="utf-8">
<title>Plover Meadow Co. — Commercial Lawn &amp; Landscape Contractor</title>
<link href="https://fonts.googleapis.com/css2?family=Poppins:wght@300;400;500;600;700;800&display=swap" rel="stylesheet">
<style>
:root{
  --lime:#a9e01b;
  --ink:#1e1f1c;
  --text:#555;
  --muted:#8a8a8a;
  --grey-bg:#f1f2ee;
  --white:#fff;
}
*{box-sizing:border-box;margin:0;padding:0}
html,body{width:1200px;height:4972px;overflow:hidden}
body{font-family:'Poppins',sans-serif;color:var(--ink);background:var(--white);position:relative}
.abs{position:absolute}
.photo{position:absolute;display:block}
.btn{display:inline-block;font-family:'Poppins',sans-serif;font-size:13px;font-weight:600;padding:10px 22px;border-radius:20px;text-decoration:none;line-height:1}
.btn-lime{background:var(--lime);color:var(--ink)}
.btn-outline{border:2px solid var(--lime);color:var(--ink);background:var(--white)}
.btn-outline-light{border:2px solid var(--lime);color:var(--white)}
.btn-dark{background:var(--ink);color:var(--white)}
.brand{display:flex;align-items:center;gap:8px;font-weight:800;font-size:22px;color:var(--lime)}
.brand-dot{width:30px;height:30px;border-radius:50%;background:var(--lime)}
.section-title{font-size:30px;font-weight:700;text-align:center;line-height:1.3}
.lead{font-size:13px;color:var(--text);line-height:1.7;text-align:center}

/* header + hero */
.hero{top:0;left:0;width:1200px;height:660px;overflow:hidden}
.hero .photo{inset:0;background:linear-gradient(180deg,#5f7a4a 0%,#7a9a5c 40%,#8f9a86 70%,#b9bbb0 100%)}
.hero-shade{position:absolute;inset:0;background:linear-gradient(180deg,rgba(0,0,0,.35),rgba(0,0,0,.1) 60%,rgba(0,0,0,0))}
.topbar{position:absolute;top:0;left:0;width:1200px;height:66px;background:var(--white)}
.topbar .brand{position:absolute;left:60px;top:14px}
.contact-line{position:absolute;right:60px;top:8px;font-size:10px;color:var(--muted);display:flex;gap:18px}
.nav{position:absolute;right:60px;top:30px;display:flex;align-items:center;gap:28px;font-size:12px;font-weight:500}
.nav a{color:var(--ink);text-decoration:none}
.hero-copy{position:absolute;top:190px;left:0;width:1200px;text-align:center;color:var(--white)}
.hero-copy h1{font-size:52px;font-weight:800;line-height:1.15}
.hero-copy h1 .amp{color:var(--lime)}
.hero-copy p{font-size:13px;width:560px;margin:22px auto 26px;line-height:1.7}
.hero-copy .btns{display:flex;justify-content:center;gap:16px}
.wave{position:absolute;left:0;width:1200px}

/* years */
.years-num{position:absolute;left:150px;top:700px;font-size:64px;font-weight:800;line-height:1}
.years-sub{position:absolute;left:150px;top:770px;font-size:20px;font-weight:500}
.years-text{position:absolute;left:640px;top:690px;width:400px;font-size:12px;color:var(--text);line-height:1.7}
.years-btn{position:absolute;left:640px;top:845px}

/* service cards */
.services{top:948px;left:0;width:1200px;height:384px;display:flex}
.svc{position:relative;width:300px;height:384px;overflow:hidden}
.svc .photo{inset:0}
.svc-label{position:absolute;bottom:22px;left:0;width:100%;text-align:center;color:var(--white);font-weight:600;font-size:18px}
.svc-feature{background:var(--lime);padding:50px 36px;text-align:center}
.svc-icon{display:block;width:80px;height:64px;margin:0 auto;border-radius:6px;background:rgba(30,31,28,.18)}
.svc-feature h3{font-size:20px;font-weight:700;margin:16px 0 10px}
.svc-feature p{font-size:11px;line-height:1.6;color:var(--ink)}
.svc-arrow{display:inline-flex;align-items:center;justify-content:center;width:70px;height:30px;border-radius:15px;background:var(--ink);margin-top:26px}

/* design build */
.build-head{top:1405px;left:200px;width:800px}
.build-head .lead{margin-top:16px}
.build-img{position:absolute;left:150px;top:1620px;width:440px;height:300px;border-radius:6px}
.feature-row{position:absolute;display:flex;gap:16px}
.feature-icon{flex:none;width:62px;height:62px;border-radius:50%;background:var(--ink);border:4px solid var(--white);display:flex;align-items:center;justify-content:center;box-shadow:0 2px 8px rgba(0,0,0,.2)}
.feature-icon.lime{background:var(--lime)}
.feature-row h4{font-size:18px;font-weight:700;margin-bottom:6px}
.feature-row p{font-size:12px;color:var(--text);line-height:1.6;width:300px}
.build-img2{position:absolute;top:2020px;height:290px;border-radius:6px}
.build-btns{position:absolute;top:2395px;left:0;width:1200px;display:flex;justify-content:center;gap:16px}

/* green dream */
.dream{top:2520px;left:0;width:1200px;height:420px;overflow:hidden}
.dream .photo{inset:0;background:linear-gradient(180deg,#3f5a2c,#2e4620 60%,#223618)}
.dream-copy{position:absolute;top:150px;width:1200px;text-align:center;color:var(--white)}
.dream-copy h2{font-size:32px;font-weight:700;line-height:1.25}
.dream-copy p{font-size:12px;width:560px;margin:14px auto 22px;line-height:1.6}
.phone-btn{display:inline-flex;align-items:center;gap:8px;background:var(--lime);color:var(--ink);font-size:14px;font-weight:700;padding:11px 24px;border-radius:24px}

/* why choose */
.why{top:2940px;left:0;width:1200px;height:700px;background:var(--grey-bg)}
.why .section-title{margin-top:90px;font-size:34px}
.why .lead{width:520px;margin:14px auto 0}
.why-grid{position:absolute;top:300px;left:150px;width:900px;display:grid;grid-template-columns:repeat(4,1fr);gap:30px}
.why-num{font-size:64px;font-weight:800;color:#e2e4dc;line-height:1}
.why-item h4{font-size:20px;font-weight:700;line-height:1.2;margin:-28px 0 14px;position:relative}
.why-item p{font-size:12px;color:var(--text);line-height:1.65}
.why-btn{position:absolute;top:605px;left:0;width:1200px;text-align:center}

/* projects */
.projects{top:3640px;left:0;width:1200px;height:520px}
.projects .section-title{margin-top:90px}
.proj{position:absolute;top:180px;height:320px}
.proj-label{position:absolute;bottom:28px;width:100%;text-align:center;color:var(--white);font-size:20px;font-weight:600}
.proj-arrow{position:absolute;top:320px;width:34px;height:34px;display:flex;align-items:center;justify-content:center}

/* testimonials */
.reviews{top:4160px;left:0;width:1200px;height:560px;overflow:hidden}
.reviews .photo{inset:0;background:linear-gradient(180deg,#2c4322,#1f3018 55%,#2a3d20)}
.reviews .section-title{position:relative;color:var(--white);margin-top:80px}
.review-grid{position:absolute;top:200px;left:150px;width:900px;display:grid;grid-template-columns:repeat(3,1fr);gap:50px;color:var(--white)}
.quote-mark{font-size:60px;font-weight:800;color:#cfd6c6;line-height:.8;height:40px}
.review p{font-size:12px;line-height:1.7;margin-top:10px;color:#e6ebe0}
.review .who{margin-top:16px;font-size:11px;color:var(--lime);font-weight:600}
.review .who span{display:block;color:#cfd6c6;font-weight:400}

/* footer */
.footer{top:4660px;left:0;width:1200px;height:268px;background:var(--white)}
.footer .brand{position:absolute;left:0;top:-10px;width:1200px;justify-content:center;font-size:20px}
.footer-grid{position:absolute;top:60px;left:150px;width:900px;display:grid;grid-template-columns:1.3fr 1fr 1fr 1.1fr;gap:30px}
.footer h5{font-size:14px;font-weight:700;margin-bottom:12px}
.footer p,.footer li{font-size:11px;color:var(--text);line-height:1.75;list-style:none}
.copyright{top:4928px;left:0;width:1200px;height:44px;background:var(--ink);color:#9a9a9a;font-size:11px;display:flex;align-items:center;padding-left:150px}
</style>
</head>
<body>

<section class="abs hero">
  <div class="photo" role="img" aria-label="Curved paver walkway through a green manicured lawn with stepping stones"></div>
  <div class="hero-shade"></div>
  <header class="topbar">
    <div class="brand"><span class="brand-dot"></span>Plover Meadow Co.</div>
    <div class="contact-line"><span>(555) 201-4830</span><span>Mon–Fri 7am–5pm</span><span>Springfield, WI</span></div>
    <nav class="nav">
      <a href="#">Home</a><a href="#">Divisions</a><a href="#">Services</a><a href="#">About Us</a><a href="#">Gallery</a><a href="#">Contact</a>
      <a href="#" class="btn btn-lime">Get A Quote</a>
    </nav>
  </header>
  <div class="hero-copy">
    <h1>Full-Service Lawn <span class="amp">&amp;</span><br>Landscape Contractor</h1>
    <p>Plover Meadow Co. strives to set the standard for the highest quality lawn and landscape products and services and to exceed our customers' expectations every time.</p>
    <div class="btns"><a class="btn btn-lime" href="#">Contact Us</a><a class="btn btn-outline-light" href="#">View Services</a></div>
  </div>
  <svg class="wave" style="top:570px" width="1200" height="90" viewBox="0 0 1200 100" preserveAspectRatio="none">
    <path fill="#fff" d="M0 60 Q40 20 80 50 Q120 10 170 45 Q220 15 260 50 Q310 20 350 48 Q400 12 450 46 Q500 18 545 50 Q590 14 640 46 Q690 20 735 50 Q780 12 830 46 Q880 18 925 50 Q970 14 1020 46 Q1070 20 1110 50 Q1160 18 1200 45 L1200 100 L0 100 Z"/>
  </svg>
</section>

<div class="years-num">15 Years</div>
<div class="years-sub">Of Professional Landscaping!</div>
<p class="years-text">Plover Meadow Co. strives to set the standard for the highest quality lawn and landscape products and services and to exceed our customers' expectations every time. Our prestigious design and maintenance crews demonstrate the value and success of our company's approach.</p>
<a class="btn btn-dark years-btn" href="#">Learn More</a>

<section class="abs services">
  <div class="svc"><div class="photo" role="img" aria-label="Freshly mowed lawn beside a stone building" style="background:linear-gradient(180deg,#8a9a86,#5d7f3e 60%,#466a2c)"></div><div class="svc-label">Turf Management</div></div>
  <div class="svc"><div class="photo" role="img" aria-label="Boulder retaining wall with shrubs and plantings" style="background:linear-gradient(180deg,#6f8a4f,#8c8576 55%,#6d6658)"></div><div class="svc-label">Hardscaping</div></div>
  <div class="svc svc-feature">
    <span class="svc-icon" role="img" aria-label="Sprinkler head illustration"></span>
    <h3>Irrigation</h3>
    <p>Plover Meadow Co. certified professionals design and install commercial and residential irrigation systems for lasting, healthy results.</p>
    <span class="svc-arrow"><svg width="18" height="12" viewBox="0 0 18 12"><path d="M1 6 H16 M11 1 L16 6 L11 11" stroke="#fff" stroke-width="2" fill="none"/></svg></span>
  </div>
  <div class="svc"><div class="photo" role="img" aria-label="Colorful flower beds with shrubs in front of a sign" style="background:linear-gradient(180deg,#7ea05a,#5e8a3c 50%,#a8604a 75%,#4e7a30)"></div><div class="svc-label">Landscaping</div></div>
</section>

<div class="abs build-head">
  <h2 class="section-title">Design, Build and Maintain Residential and<br>Commercial Landscapes</h2>
  <p class="lead">To be recognized by our customers for providing the best value in products and services. To be recognized by our employees as a quality company where they can develop and grow. To grow with the green industry and continue to be a successful and profitable business.</p>
</div>
<div class="photo build-img" role="img" aria-label="Company work truck with crew members at a commercial site" style="background:linear-gradient(180deg,#8fb3d4,#c9ccc6 45%,#6f8a55 80%)"></div>
<div class="feature-row" style="left:560px;top:1640px">
  <span class="feature-icon"><svg width="28" height="28" viewBox="0 0 28 28"><path d="M4 14 L14 5 L24 14 M7 12 V23 H21 V12" fill="none" stroke="#a9e01b" stroke-width="2.5"/></svg></span>
  <div><h4>Residential</h4><p>Plover Meadow Co. offers landscape services to complement your property both structurally and aesthetically.</p></div>
</div>
<div class="feature-row" style="left:560px;top:1760px">
  <span class="feature-icon lime"><svg width="28" height="28" viewBox="0 0 28 28"><path d="M5 24 V8 H15 V24 M15 13 H23 V24 M3 24 H25" fill="none" stroke="#1e1f1c" stroke-width="2.5"/></svg></span>
  <div><h4>Commercial</h4><p>Plover Meadow Co. provides property management services for large and small organizations varying in scale and complexity.</p></div>
</div>
<div class="feature-row" style="left:150px;top:2060px;flex-direction:row-reverse;width:460px">
  <span class="feature-icon"><svg width="28" height="28" viewBox="0 0 28 28"><path d="M4 24 H24 M6 24 V12 M11 24 V12 M17 24 V12 M22 24 V12 M3 11 L14 4 L25 11 Z" fill="none" stroke="#a9e01b" stroke-width="2.2"/></svg></span>
  <div><h4>Government</h4><p>Plover Meadow Co. provides landscaping solutions for government and military properties including...</p></div>
</div>
<div class="feature-row" style="left:150px;top:2180px;flex-direction:row-reverse;width:460px">
  <span class="feature-icon"><svg width="28" height="28" viewBox="0 0 28 28"><circle cx="14" cy="14" r="10" fill="none" stroke="#a9e01b" stroke-width="2.2"/><path d="M14 4 V24 M4 14 H24" stroke="#a9e01b" stroke-width="2"/></svg></span>
  <div><h4>Sports Fields</h4><p>Plover Meadow Co. specializes in the new construction of sports fields for schools from designing and grading to irrigation...</p></div>
</div>
<div class="photo build-img2" role="img" aria-label="Lush hosta garden bed along a walkway" style="left:610px;width:300px;background:linear-gradient(180deg,#4d7a32,#3b6526 60%,#2c4d1c)"></div>
<div class="photo build-img2" role="img" aria-label="Landscaped commercial building entrance with lawn" style="left:920px;width:130px;background:linear-gradient(180deg,#9ab0c2,#6a8a4e 60%,#4a6a30)"></div>
<div class="build-btns"><a class="btn btn-lime" href="#">Contact Us</a><a class="btn btn-outline" href="#">View Services</a></div>

<section class="abs dream">
  <div class="photo" role="img" aria-label="Wide green lawn lined with mature trees"></div>
  <svg class="wave" style="top:0" width="1200" height="80" viewBox="0 0 1200 80" preserveAspectRatio="none">
    <path fill="#fff" d="M0 0 H1200 V30 Q1160 60 1110 34 Q1070 62 1020 36 Q970 64 925 34 Q880 60 830 36 Q780 66 735 32 Q690 60 640 36 Q590 64 545 32 Q500 60 450 36 Q400 66 350 34 Q310 60 260 32 Q220 62 170 36 Q120 66 80 32 Q40 58 0 34 Z"/>
  </svg>
  <div class="dream-copy">
    <h2>We're Here to Help &amp; Grow<br>Your Green Dream</h2>
    <p>Plover Meadow Co. strives to set the standard for the highest quality lawn and landscape products and services and to exceed our customers' expectations every time.</p>
    <span class="phone-btn"><svg width="16" height="16" viewBox="0 0 24 24"><path fill="#1e1f1c" d="M6.6 10.8a15.1 15.1 0 006.6 6.6l2.2-2.2a1 1 0 011-.25 11.4 11.4 0 003.6.57 1 1 0 011 1V20a1 1 0 01-1 1A17 17 0 013 4a1 1 0 011-1h3.5a1 1 0 011 1c0 1.25.2 2.45.57 3.57a1 1 0 01-.25 1z"/></svg>Call Us At: (555) 201-4830 / (555) 318-7742</span>
  </div>
</section>

<section class="abs why">
  <h2 class="section-title">Why Choose Us</h2>
  <p class="lead">Plover Meadow Co. is a full service lawn and landscape contractor providing design, installation, and maintenance services.</p>
  <div class="why-grid">
    <div class="why-item"><div class="why-num">01</div><h4>Specialized Company</h4><p>Plover Meadow Co. strives to set the standard for the highest quality lawn and landscape products and services and to exceed our customers' expectations every time.</p></div>
    <div class="why-item"><div class="why-num">02</div><h4>Free Consultations</h4><p>Call our office to set up a time to meet with one of our qualified professionals. They will walk your property with you to help make those decisions.</p></div>
    <div class="why-item"><div class="why-num">03</div><h4>Dependable Services</h4><p>Communication is highly valued at our company. From start to finish our clients will be kept up to date on their project.</p></div>
    <div class="why-item"><div class="why-num">04</div><h4>Reputable Company</h4><p>With 15 years of experience in the landscaping construction business, we have built a reputation for superior projects and service.</p></div>
  </div>
  <div class="why-btn"><a class="btn btn-lime" href="#">Get A Free Quote</a></div>
</section>

<section class="abs projects">
  <h2 class="section-title">Explore Our Recent Projects</h2>
  <div class="photo proj" role="img" aria-label="Residential home with landscaped front yard" style="left:0;width:250px;background:linear-gradient(180deg,#c9cfd2,#a9b0a8 50%,#6f8e4a)"></div>
  <div class="photo proj" role="img" aria-label="Backyard pool with patio furniture and plantings" style="left:270px;width:660px;top:150px;height:360px;background:linear-gradient(180deg,#6e8e52,#6aa7c4 50%,#c8b8a0 80%,#7a6a58)"><div class="proj-label">Residential</div></div>
  <div class="photo proj" role="img" aria-label="Crew working on a commercial landscape site" style="left:950px;width:250px;background:linear-gradient(180deg,#b8c6cc,#7e9a60 55%,#4f7034)"></div>
  <span class="proj-arrow" style="left:240px"><svg width="20" height="20" viewBox="0 0 20 20"><path d="M13 3 L6 10 L13 17" stroke="#fff" stroke-width="2.5" fill="none"/></svg></span>
  <span class="proj-arrow" style="left:926px"><svg width="20" height="20" viewBox="0 0 20 20"><path d="M7 3 L14 10 L7 17" stroke="#fff" stroke-width="2.5" fill="none"/></svg></span>
</section>

<section class="abs reviews">
  <div class="photo" role="img" aria-label="Dim green lawn and trees background"></div>
  <h2 class="section-title">What Customer Say About Us</h2>
  <div class="review-grid">
    <div class="review"><div class="quote-mark">“</div><p>I want to thank the crew again for finishing and checking the work performed recently. All areas look very nice and it looks like we received more than worth of the playground fiber under every tree.</p><div class="who">Dana Whitlow<span>Riverside School District</span></div></div>
    <div class="review"><div class="quote-mark">“</div><p>As part of the Ridgeway Development Company, I have been extremely pleased with the dramatic improvements to the landscape within the community evident since the beginning of our partnership.</p><div class="who">Sam Kellerman<span>Ridgeway Development Company</span></div></div>
    <div class="review"><div class="quote-mark">“</div><p>I have been working with Plover Meadow Co. for several years. As a building development firm I understand the importance of landscaping on our projects. They have provided expert service.</p><div class="who">Lena Marsh<span>Marsh Construction Company</span></div></div>
  </div>
</section>

<footer class="abs footer">
  <svg class="wave" style="top:-40px" width="1200" height="60" viewBox="0 0 1200 60" preserveAspectRatio="none">
    <path fill="#fff" d="M0 40 Q40 10 80 34 Q120 6 170 32 Q220 8 260 34 Q310 10 350 32 Q400 6 450 32 Q500 10 545 34 Q590 6 640 32 Q690 10 735 34 Q780 6 830 32 Q880 10 925 34 Q970 6 1020 32 Q1070 10 1110 34 Q1160 10 1200 30 L1200 60 L0 60 Z"/>
  </svg>
  <div class="brand"><span class="brand-dot"></span>Plover Meadow Co.</div>
  <div class="footer-grid">
    <div><h5>Plover Meadow Co.</h5><p>Plover Meadow Co. strives to set the standard for the highest quality lawn and landscape products and services and to exceed our customers' expectations every time.</p></div>
    <div><h5>Quick Links</h5><ul><li>About Us</li><li>Divisions</li><li>Certifications</li><li>Gallery</li></ul></div>
    <div><h5>Our Services</h5><ul><li>Turf Management</li><li>Hardscaping</li><li>Irrigation</li><li>Landscaping</li></ul></div>
    <div><h5>Contact Information</h5><p>Plover Meadow Co.<br>2270 Orchard Lane<br>Springfield, WI 54000<br>P (555) 201-4830<br>F (555) 318-7742<br>www.plovermeadowco.com</p></div>
  </div>
</footer>
<div class="abs copyright">Copyright 2024 Plover Meadow Co. All Rights Reserved.</div>

</body>
</html>
```